Basic Website for Vending Machine Business

We need a website designed for our vending machine business, Munchtronix, which is located in Ottawa, Canada. We requires a few links to standard sub-pages (About Us, Machines, Request a Machine, Report a Problem, Contact Us, etc.). We want it to be fun and simple. Possibly involve a vending machine in some way - make selections inside the machine the links to sub pages? Just an idea, we are very flexible though...please be creative. Attached are the drafts of our logo, we will provide the official copies of logo in near future. Key for our website is we want it visually appealing and fun, as opposed to formal.
Some slogans you may wish to use:
- Vend. Snack. Smile.
- Shop. Snack. Smile.
Target Market(s)
Small and medium size business owners.
Industry/Entity Type
Business

```html
<!DOCTYPE html>
<html lang="en">
<head>
<meta charset="utf-8">
<title>Munchtronix – Vending Machines</title>
<link rel="stylesheet" href="https://fonts.googleapis.com/css2?family=Raleway:wght@300;400;500&family=Lato:ital,wght@0,400;0,700;1,400&display=swap">
<style>
:root{
  --teal:#66aca4;
  --blue:#1456a8;
  --blue-dark:#0f4688;
  --ink:#333;
  --muted:#555;
  --gray-band:#eeeeee;
  --footer:#6e6e6e;
  --white:#fff;
}
*{box-sizing:border-box;margin:0;padding:0}
html,body{width:1200px;height:2662px;overflow:hidden}
body{position:relative;background:var(--white);font-family:'Lato',sans-serif;color:var(--ink)}
.abs{position:absolute}

/* header */
.header-band{left:0;top:0;width:1200px;height:547px;background:var(--teal)}
.brand{left:125px;top:38px;display:flex;flex-direction:column;align-items:center;gap:6px;color:var(--white);font-family:'Lato',sans-serif;font-weight:700;font-size:22px}
.brand-mark{width:44px;height:44px;border-radius:50%;background:var(--white)}
.nav{left:342px;top:53px;display:flex;align-items:center;height:41px;font-family:'Lato',sans-serif;font-size:15px;color:var(--white)}
.nav a{color:var(--white);text-decoration:none;margin-right:38px}
.nav a.active{background:var(--blue);padding:11px 20px;border-radius:3px;margin-right:28px}

/* hero */
.hero{left:100px;top:137px;width:1000px;height:536px;background:linear-gradient(100deg,#1c1d22 0%,#3a3530 45%,#6b625a 70%,#2a2a2e 100%)}
.hero-shadow{left:120px;top:673px;width:960px;height:28px;background:radial-gradient(ellipse at top,rgba(0,0,0,.35),rgba(0,0,0,0) 70%)}
.hero-caption{left:205px;top:320px;width:383px;height:184px;background:rgba(40,40,40,.55);padding:28px 16px;color:var(--white)}
.hero-caption h1{font-family:'Raleway',sans-serif;font-weight:400;font-size:25px;line-height:34px}
.hero-caption p{font-family:'Raleway',sans-serif;font-size:16px;line-height:24px;margin-top:16px}
.btn{display:inline-flex;align-items:center;gap:7px;background:var(--blue);color:var(--white);font-family:'Lato',sans-serif;font-weight:700;font-size:13px;text-transform:uppercase;border-radius:3px;justify-content:center;box-shadow:0 2px 0 var(--blue-dark)}
.hero-btn{left:207px;top:527px;width:137px;height:44px}
.slide-arrow{top:385px;width:43px;height:42px;background:var(--blue);display:flex;align-items:center;justify-content:center}
.slide-arrow.left{left:82px}
.slide-arrow.right{left:1075px}

/* section titles */
.section-title{left:0;width:1200px;text-align:center;font-family:'Raleway',sans-serif;font-weight:400;font-size:35px;color:var(--blue)}
.title-rule{left:510px;width:180px;height:12px}
.welcome-sub{left:0;top:798px;width:1200px;text-align:center;font-family:'Raleway',sans-serif;font-weight:500;font-size:23px;color:var(--blue)}
.welcome-text{left:205px;top:840px;width:790px;text-align:center;font-size:12.5px;line-height:17px;color:var(--muted)}

/* about */
.about-band{left:0;top:929px;width:1200px;height:463px;background:var(--gray-band)}
.about-photo{left:125px;top:1041px;width:462px;height:308px;border:3px solid var(--blue);background:linear-gradient(90deg,#2a2e44 0%,#4c5a80 35%,#c9a24a 60%,#5b8aa8 85%,#2a2e44 100%)}
.about-head{left:612px;top:1042px;font-family:'Raleway',sans-serif;font-weight:500;font-size:19px;color:var(--blue)}
.about-text{left:612px;top:1078px;width:463px;font-size:12.5px;line-height:14.5px;color:var(--muted);text-align:justify}
.about-btn{left:612px;top:1289px;width:138px;height:43px}

/* machines */
.machine-card{top:1506px;width:217px;height:395px;background:var(--blue);padding:8px;color:var(--white);text-align:center}
.machine-card .shot{height:216px;background:var(--white);display:flex;align-items:center;justify-content:center}
.machine-card .shot div{width:110px;height:198px}
.machine-card h3{font-family:'Lato',sans-serif;font-style:italic;font-weight:400;font-size:21px;line-height:27px;margin-top:11px}
.machine-card p{font-size:12px;line-height:14px;margin-top:10px;height:42px;overflow:hidden}
.machine-card .more{display:inline-flex;align-items:center;gap:7px;font-weight:700;font-size:12.5px;margin-top:18px}
.card-shadow{top:1901px;width:217px;height:20px;background:radial-gradient(ellipse at top,rgba(0,0,0,.4),rgba(0,0,0,0) 70%)}

/* newsletter */
.newsletter{left:100px;top:1958px;width:1000px;height:98px;background:var(--white);box-shadow:0 6px 14px rgba(0,0,0,.18)}
.news-title{left:125px;top:1990px;font-family:'Raleway',sans-serif;font-weight:500;font-size:23px;color:var(--blue)}
.news-input{left:450px;top:1982px;width:446px;height:49px;border:1.5px solid #999;border-right:none;font-size:13px;padding:16px 14px;color:#444}
.news-send{left:896px;top:1982px;width:97px;height:49px;background:var(--blue);display:flex;align-items:center;justify-content:center}
.page-curl{left:1062px;top:1958px;width:40px;height:98px}

/* footer columns */
.col-title{top:2110px;font-family:'Raleway',sans-serif;font-weight:400;font-size:25px;color:var(--blue)}
.contact-item{left:125px;display:flex;gap:18px;align-items:flex-start;font-size:14px;line-height:20px;color:var(--ink)}
.contact-item svg{flex:none;margin-top:2px}
.info-list{left:450px;top:2166px;list-style:none}
.info-list li{display:flex;align-items:center;gap:13px;font-size:14px;height:26.5px}
.field{border:1.5px solid #777;border-radius:3px;font-size:10.5px;padding:7px 9px;color:#333;background:var(--white)}
.submit-btn{left:694px;top:2314px;width:91px;height:27px;font-size:12px}

/* bottom footer */
.foot-band{left:0;top:2382px;width:1200px;height:280px;background:var(--footer)}
.foot-brand{left:0;top:2426px;width:1200px;display:flex;flex-direction:column;align-items:center;gap:8px;color:var(--white);font-weight:700;font-size:30px}
.foot-brand .brand-mark{width:50px;height:50px}
.copyright{left:0;top:2536px;width:1200px;text-align:center;color:var(--white);font-size:11px;font-style:italic}
.social{left:420px;top:2559px;display:flex;gap:15px}
.social span{width:60px;height:60px;border-radius:50%;background:var(--blue);display:block}
</style>
</head>
<body>

<div class="abs header-band"></div>
<div class="abs brand"><span class="brand-mark"></span><span>Munchtronix</span></div>
<nav class="abs nav">
  <a class="active">Home</a><a>About Us</a><a>Machines</a><a>Request a Machine</a><a>Report a Problem</a><a>Contact Us</a>
</nav>

<div class="abs hero" role="img" aria-label="Night-time station platform with a lit snack vending machine"></div>
<div class="abs hero-shadow"></div>
<div class="abs hero-caption">
  <h1>The Perfect Vending Machine To Suit Your Business</h1>
  <p>A great selection of high quality vending machines</p>
</div>
<div class="abs btn hero-btn">Learn More
  <svg width="12" height="12" viewBox="0 0 12 12"><circle cx="6" cy="6" r="6" fill="#fff"/><path d="M5 3.5 7.5 6 5 8.5" stroke="#1456a8" stroke-width="1.8" fill="none"/></svg></div>
<div class="abs slide-arrow left"><svg width="14" height="14" viewBox="0 0 14 14"><path d="M9 2 4 7l5 5" stroke="#fff" stroke-width="2.5" fill="none"/></svg></div>
<div class="abs slide-arrow right"><svg width="14" height="14" viewBox="0 0 14 14"><path d="M5 2l5 5-5 5" stroke="#fff" stroke-width="2.5" fill="none"/></svg></div>

<h2 class="abs section-title" style="top:736px">Wel come !</h2>
<svg class="abs title-rule" style="top:776px" viewBox="0 0 180 12"><line x1="0" y1="6" x2="180" y2="6" stroke="#1456a8" stroke-width="1.5"/><path d="M90 1 95 6 90 11 85 6z" fill="#1456a8"/></svg>
<div class="abs welcome-sub">A Great Selection Of High Quality Vending Machines</div>
<p class="abs welcome-text">Lorem ipsum dolor sit amet conse ctetur adipisicing elit, sed do eiusmod tempor incididunt ut labore et dolore magna aliqua. Ut enim ad minim veniam, quis nostrud exercitation ullamco laboris nisi ut aliquip ex ea commodo consequat. Duis aute irure dolor in repre­henderit in voluptate velit esse cillum dolore eu fugiat.</p>

<div class="abs about-band"></div>
<h2 class="abs section-title" style="top:955px">About Us</h2>
<svg class="abs title-rule" style="top:995px" viewBox="0 0 180 12"><line x1="0" y1="6" x2="180" y2="6" stroke="#1456a8" stroke-width="1.5"/><path d="M90 1 95 6 90 11 85 6z" fill="#1456a8"/></svg>
<div class="abs about-photo" role="img" aria-label="Woman choosing drinks from a brightly lit vending machine"></div>
<h3 class="abs about-head">Excepteur sint occaecat cupidatat non proident sunt</h3>
<p class="abs about-text">Lorem ipsum dolor sit amet conse ctetur adipisicing elit, sed do eiusmod tempor incididunt ut labore et dolore magna aliqua. Ut enim ad minim veniam, quis nostrud exercitation ullamco laboris nisi ut aliquip ex ea. Duis aute irure dolor in reprehenderit in voluptate velit esse cillum dolore eu fugiat nulla pariatur. Excepteur sint occaecat cupidatat non proident, sunt in culpa.Lorem ipsum dolor sit amet conse ctetur adipisicing elit, sed do eiusmod tempor incididunt ut labore et dolore magna aliqua. Ut enim ad minim veniam, quis nostrud exercitation ullamco laboris nisi ut aliquip ex ea. Duis aute irure dolor in reprehenderit in voluptate velit esse cillum dolore eu fugiat nulla pariatur. Excepteur sint occaecat cupidatat non proident, sunt in culpa.</p>
<div class="abs btn about-btn">Read More
  <svg width="12" height="12" viewBox="0 0 12 12"><circle cx="6" cy="6" r="6" fill="#fff"/><path d="M5 3.5 7.5 6 5 8.5" stroke="#1456a8" stroke-width="1.8" fill="none"/></svg></div>

<h2 class="abs section-title" style="top:1425px">Machines</h2>
<svg class="abs title-rule" style="top:1466px" viewBox="0 0 180 12"><line x1="0" y1="6" x2="180" y2="6" stroke="#1456a8" stroke-width="1.5"/><path d="M90 1 95 6 90 11 85 6z" fill="#1456a8"/></svg>

<div class="abs machine-card" style="left:125px">
  <div class="shot"><div role="img" aria-label="Black snack vending machine" style="background:linear-gradient(180deg,#222,#555 50%,#222)"></div></div>
  <h3>Snacks Vending<br>Machines</h3>
  <p>Lorem ipsum dolor sit amet conse ctetur adipisicing elit, sed do eius­mod tempor incididunt ut labore et</p>
  <span class="more">READ MORE <svg width="12" height="12" viewBox="0 0 12 12"><circle cx="6" cy="6" r="6" fill="#fff"/><path d="M5 3.5 7.5 6 5 8.5" stroke="#1456a8" stroke-width="1.8" fill="none"/></svg></span>
</div>
<div class="abs machine-card" style="left:369px">
  <div class="shot"><div role="img" aria-label="Red cold drinks vending machine" style="background:linear-gradient(90deg,#b3121a,#e23a3a 60%,#8e0e14)"></div></div>
  <h3>Drinks Vending<br>Machines</h3>
  <p>Lorem ipsum dolor sit amet conse ctetur adipisicing elit, sed do eius­mod tempor incididunt ut labore et</p>
  <span class="more">READ MORE <svg width="12" height="12" viewBox="0 0 12 12"><circle cx="6" cy="6" r="6" fill="#fff"/><path d="M5 3.5 7.5 6 5 8.5" stroke="#1456a8" stroke-width="1.8" fill="none"/></svg></span>
</div>
<div class="abs machine-card" style="left:612px">
  <div class="shot"><div role="img" aria-label="Black coffee vending machine" style="background:linear-gradient(90deg,#3a6fa8,#c9a870 45%,#1d1d1d 70%)"></div></div>
  <h3>Coffee Vending<br>Machines</h3>
  <p>Lorem ipsum dolor sit amet conse ctetur adipisicing elit, sed do eius­mod tempor incididunt ut labore et</p>
  <span class="more">READ MORE <svg width="12" height="12" viewBox="0 0 12 12"><circle cx="6" cy="6" r="6" fill="#fff"/><path d="M5 3.5 7.5 6 5 8.5" stroke="#1456a8" stroke-width="1.8" fill="none"/></svg></span>
</div>
<div class="abs machine-card" style="left:856px">
  <div class="shot"><div role="img" aria-label="Soda fountain dispenser with glasses" style="width:160px;height:170px;background:linear-gradient(180deg,#f0b84a,#e67e3a 35%,#9aa0a8 65%,#5a5e66)"></div></div>
  <h3>Soda Vending<br>Machines</h3>
  <p>Lorem ipsum dolor sit amet conse ctetur adipisicing elit, sed do eius­mod tempor incididunt ut labore et</p>
  <span class="more">READ MORE <svg width="12" height="12" viewBox="0 0 12 12"><circle cx="6" cy="6" r="6" fill="#fff"/><path d="M5 3.5 7.5 6 5 8.5" stroke="#1456a8" stroke-width="1.8" fill="none"/></svg></span>
</div>
<div class="abs card-shadow" style="left:125px"></div>
<div class="abs card-shadow" style="left:369px"></div>
<div class="abs card-shadow" style="left:612px"></div>
<div class="abs card-shadow" style="left:856px"></div>

<div class="abs newsletter"></div>
<svg class="abs page-curl" viewBox="0 0 40 98"><path d="M40 0V60Q30 92 0 98H40Z" fill="#e4e4e4"/><path d="M40 60Q30 92 0 98Q26 80 40 60Z" fill="#cfcfcf"/></svg>
<div class="abs news-title">Subscribe To The Newsletter</div>
<div class="abs news-input">Enter Your Email Address</div>
<div class="abs news-send"><svg width="32" height="28" viewBox="0 0 32 28"><path d="M31 1 1 13l9 3 2 10 5-7 8 5z" fill="#fff"/><path d="M10 16 31 1 14 19" stroke="#1456a8" stroke-width="1.5" fill="none"/></svg></div>

<h3 class="abs col-title" style="left:125px">Contact Us</h3>
<div class="abs contact-item" style="top:2170px">
  <svg width="12" height="16" viewBox="0 0 12 16"><path d="M6 0a6 6 0 0 0-6 6c0 4 6 10 6 10s6-6 6-10a6 6 0 0 0-6-6z" fill="#1456a8"/><circle cx="6" cy="6" r="2.2" fill="#fff"/></svg>
  <span>48 Maple Lane, Ottawa Ontario<br>Canada</span></div>
<div class="abs contact-item" style="top:2230px;font-size:15px">
  <svg width="16" height="16" viewBox="0 0 16 16"><path d="M3 0 6 4 4 6q2 4 6 6l2-2 4 3-2 3Q7 16 0 3z" fill="#1456a8"/></svg>
  <span>hello@munchtronix.ca</span></div>
<div class="abs contact-item" style="top:2272px">
  <svg width="18" height="13" viewBox="0 0 18 13"><rect x="1" y="1" width="16" height="11" fill="none" stroke="#1456a8" stroke-width="1.8"/><path d="M1 1l8 6 8-6" stroke="#1456a8" stroke-width="1.8" fill="none"/></svg>
  <span>+1 (613) 555 0142</span></div>
<div class="abs contact-item" style="top:2313px">
  <svg width="20" height="16" viewBox="0 0 20 16"><rect x="5" y="0" width="10" height="5" fill="#1456a8"/><rect x="0" y="5" width="20" height="8" rx="1" fill="#1456a8"/><rect x="5" y="10" width="10" height="6" fill="#fff" stroke="#1456a8" stroke-width="1.5"/></svg>
  <span>+1 613-555-0198</span></div>

<h3 class="abs col-title" style="left:450px">Information</h3>
<ul class="abs info-list">
  <li><svg width="12" height="12" viewBox="0 0 12 12"><circle cx="6" cy="6" r="6" fill="#1456a8"/><path d="M5 3.5 7.5 6 5 8.5" stroke="#fff" stroke-width="1.8" fill="none"/></svg>Specials</li>
  <li><svg width="12" height="12" viewBox="0 0 12 12"><circle cx="6" cy="6" r="6" fill="#1456a8"/><path d="M5 3.5 7.5 6 5 8.5" stroke="#fff" stroke-width="1.8" fill="none"/></svg>New products</li>
  <li><svg width="12" height="12" viewBox="0 0 12 12"><circle cx="6" cy="6" r="6" fill="#1456a8"/><path d="M5 3.5 7.5 6 5 8.5" stroke="#fff" stroke-width="1.8" fill="none"/></svg>Best sellers</li>
  <li><svg width="12" height="12" viewBox="0 0 12 12"><circle cx="6" cy="6" r="6" fill="#1456a8"/><path d="M5 3.5 7.5 6 5 8.5" stroke="#fff" stroke-width="1.8" fill="none"/></svg>Our stores</li>
  <li><svg width="12" height="12" viewBox="0 0 12 12"><circle cx="6" cy="6" r="6" fill="#1456a8"/><path d="M5 3.5 7.5 6 5 8.5" stroke="#fff" stroke-width="1.8" fill="none"/></svg>Contact us</li>
  <li><svg width="12" height="12" viewBox="0 0 12 12"><circle cx="6" cy="6" r="6" fill="#1456a8"/><path d="M5 3.5 7.5 6 5 8.5" stroke="#fff" stroke-width="1.8" fill="none"/></svg>Pages configuration</li>
  <li><svg width="12" height="12" viewBox="0 0 12 12"><circle cx="6" cy="6" r="6" fill="#1456a8"/><path d="M5 3.5 7.5 6 5 8.5" stroke="#fff" stroke-width="1.8" fill="none"/></svg>Sitemap</li>
</ul>

<h3 class="abs col-title" style="left:694px">Report a Problem</h3>
<div class="abs field" style="left:694px;top:2168px;width:186px;height:29px">First Name</div>
<div class="abs field" style="left:888px;top:2168px;width:187px;height:29px">Last Name</div>
<div class="abs field" style="left:694px;top:2208px;width:186px;height:28px">Number</div>
<div class="abs field" style="left:888px;top:2208px;width:187px;height:28px">Email Address</div>
<div class="abs field" style="left:694px;top:2247px;width:381px;height:55px">Message</div>
<div class="abs btn submit-btn">Submit</div>

<div class="abs foot-band"></div>
<div class="abs foot-brand"><span class="brand-mark"></span><span>Munchtronix</span></div>
<div class="abs copyright">© copyright 2015 munchtronix. &nbsp;|&nbsp; All Rights Reserved. &nbsp;|&nbsp; Privacy Policy</div>
<div class="abs social" aria-label="Social network links"><span></span><span></span><span></span><span></span><span></span></div>

</body>
</html>
```